Thornfield Marsh, LLC Website

We are a small law firm in need of a website that contains the following:
1. Attractive main page
2. About us/attorney info for three people: Leonard Thornfield (attorney), Brent Marsh (attorney), and Melinda Carrow (legal assistant). We have bio's ready to submit.
3. Blog/video page. We'd like to post blogs and videos to help drive traffic
4. Multidistrict Litigation and Class Actions page, where we post information regarding active MDLs and Class actions that we are doing intake on.
Updates

Can you also please use the color "gold" in the design and logo? Thanks.

Industry/Entity Type

Legal

Coding

Coded - Design and coding required

Number of Pages Required

1 page

Colors
0054AA
0677BA
7BADD7
CADEEF
E8F1F8

Requirements
Must have
• 1. Attractive main page 2. About us/attorney info for three people: Leonard Thornfield (attorney), Brent Marsh (attorney), and Melinda Carrow (legal assistant). We have bio's ready to submit. 3. Blog/video page. We'd like to post blogs and videos to help drive traffic 4. Multidistrict Litigation and Class Actions page, where we post information regarding active MDLs and Class actions that we are doing intake on.

```html
<!DOCTYPE html>
<html lang="en">
<head>
<meta charset="utf-8">
<title>Thornfield Marsh, LLC — Lawyers</title>
<link href="https://fonts.googleapis.com/css2?family=Jost:wght@400;500;600;700&display=swap" rel="stylesheet">
<style>
:root{
  --navy:#0b1f8f;
  --navy-deep:#07166e;
  --sky:#1ea7f0;
  --gold:#c9a33a;
  --ink:#1a1a1a;
  --muted:#7a7a7a;
  --paper:#f7f7f7;
  --mist:#eef2fc;
  --night:#121212;
  --white:#ffffff;
}
*{box-sizing:border-box;margin:0;padding:0}
html,body{width:1200px;height:4213px;overflow:hidden}
body{font-family:'Jost',sans-serif;color:var(--ink);background:var(--white);position:relative}
section,header,nav,footer{position:absolute;left:0;width:1200px}
.abs{position:absolute}
p{line-height:1.75}

/* header */
.topbar{top:0;height:95px;background:var(--white)}
.brand{left:45px;top:15px;width:345px;height:63px;border:3px solid var(--navy);display:flex;align-items:center;gap:12px;padding-left:14px;white-space:nowrap}
.brand-mark{width:34px;height:34px;background:var(--gold);flex:none}
.brand-name{font-size:19px;font-weight:600;color:var(--navy);letter-spacing:.2px;white-space:nowrap}
.contact-chip{display:flex;align-items:center;gap:14px;top:22px}
.chip-icon{width:56px;height:56px;border-radius:50%;background:var(--sky);display:flex;align-items:center;justify-content:center}
.chip-label{font-size:16px;color:var(--sky);font-weight:500;line-height:1.2}
.chip-value{font-size:17px;color:#444;font-weight:500;line-height:1.3}

.mainnav{top:95px;height:69px;background:var(--navy);display:flex;justify-content:center;align-items:center;gap:74px;border-bottom:2px solid var(--gold)}
.mainnav a{color:var(--white);text-decoration:none;font-size:15px;font-weight:500;letter-spacing:.4px}

/* hero */
.hero{top:164px;height:586px}
.hero-photo{inset:0;background:linear-gradient(100deg,#e9edf2 0%,#c9d3de 30%,#aab6c4 55%,#8b7a68 75%,#c7ccd3 100%)}
.hero-title{left:58px;top:150px;font-size:42px;font-weight:700;line-height:1.2;color:#141a3a}
.hero-text{left:58px;top:260px;width:380px;font-size:11.5px;color:#333}
.btn{display:inline-flex;align-items:center;justify-content:center;color:var(--white);font-weight:600;font-size:14px;letter-spacing:.3px}
.btn-sky{background:var(--sky)}
.btn-navy{background:var(--navy)}

.section-title{left:0;width:100%;text-align:center;font-size:34px;font-weight:700;color:var(--navy)}
.title-rule{height:4px;background:var(--navy)}
.lead{left:0;width:100%;text-align:center;font-size:12px;color:var(--muted)}

/* why us */
.why{top:750px;height:540px;background:var(--paper)}
.feature{width:237px;height:260px;background:var(--white);text-align:center;box-shadow:0 2px 10px rgba(0,0,0,.04)}
.feature svg{margin-top:12px}
.feature h3{font-size:15px;font-weight:600;margin-top:8px}
.feature p{font-size:10px;color:var(--muted);padding:8px 30px 0;line-height:1.75}
.feature a{display:inline-block;margin-top:12px;font-size:10px;font-weight:600;color:var(--sky);text-decoration:underline}

/* about */
.about{top:1290px;height:478px;background:var(--white);overflow:hidden}
.about-photo{left:83px;top:30px;width:449px;height:342px;background:linear-gradient(135deg,#d9a76a 0%,#8b5a32 45%,#2b1d14 100%)}
.about-title{left:622px;top:65px;font-size:32px;font-weight:700;color:var(--navy);white-space:nowrap}
.about-text{left:622px;top:135px;width:520px;font-size:10.5px;color:#555}
.about-text p+p{margin-top:4px}

/* practice */
.practice{top:1768px;height:657px;background:var(--mist)}
.practice-card{top:275px;height:264px;background:var(--white);display:flex}
.practice-photo{width:209px;height:264px;flex:none}
.practice-body{padding:30px 22px 0 24px}
.practice-body h3{font-size:16px;font-weight:700;color:var(--navy)}
.practice-body p{font-size:10px;color:#666;margin-top:12px;line-height:1.65}
.practice-body .btn{margin-top:14px;width:137px;height:31px}

/* team */
.team{top:2425px;height:633px;background:linear-gradient(180deg,#1a2ea0 0%,#13279a 40%,#0f23a0 100%)}
.member{top:220px;width:237px;height:337px;background:var(--white);text-align:center}
.avatar{width:145px;height:145px;border-radius:50%;background:linear-gradient(180deg,#d8d8d8,#b9b9b9);margin:46px auto 0}
.member h3{font-size:15px;font-weight:600;margin-top:22px;letter-spacing:.2px}
.member .role{display:inline-block;font-size:13px;color:var(--sky);text-decoration:underline;margin-top:5px}
.member p{font-size:10.5px;color:#777;padding:6px 24px 0;line-height:1.5}

/* blog */
.blog{top:3058px;height:752px;background:var(--white)}
.post{top:287px;width:244px;height:360px;background:var(--white);box-shadow:0 4px 18px rgba(0,0,0,.07)}
.post-photo{height:212px}
.post h3{font-size:15px;font-weight:600;padding:18px 16px 0}
.post-meta{display:flex;gap:24px;padding:8px 16px 0;font-size:8px;color:var(--sky);align-items:center}
.post-meta span{display:flex;align-items:center;gap:6px}
.post p{font-size:10px;color:#777;padding:8px 16px 0;line-height:1.6}

/* footer */
.site-footer{top:3810px;height:403px;background:var(--night);color:#ddd}
.foot-brand{left:85px;top:105px;width:265px;height:47px;border:2px solid var(--navy);display:flex;align-items:center;gap:10px;padding-left:12px;white-space:nowrap}
.foot-brand .brand-mark{width:24px;height:24px}
.foot-brand .brand-name{font-size:15px;color:var(--sky);font-weight:600}
.foot-about{left:90px;top:162px;width:300px;font-size:10.5px;line-height:1.6;color:#ddd}
.social{left:90px;top:248px;display:flex;gap:38px}
.social span{width:18px;height:18px;border-radius:50%;border:2px solid var(--sky)}
.foot-head{font-size:17px;font-weight:700;color:var(--white);letter-spacing:.3px}
.foot-links{list-style:none;margin-top:14px}
.foot-links li{font-size:15px;display:flex;align-items:center;gap:8px;height:30px;color:#ddd}
.foot-contact{list-style:none;margin-top:18px}
.foot-contact li{font-size:11px;display:flex;align-items:center;gap:12px;height:40px;color:#ddd}
.subscribe-field{width:145px;height:26px;background:var(--white);margin-top:20px}
.subscribe-btn{width:145px;height:26px;background:var(--sky);margin-top:12px;font-size:11px;color:var(--white);font-weight:600;display:flex;align-items:center;justify-content:center}
.foot-rule{left:95px;top:340px;width:985px;height:1px;background:#3a3a3a}
.copyright{left:0;width:100%;top:370px;text-align:center;font-size:11px;color:#ccc}
</style>
</head>
<body>

<header class="topbar">
  <div class="brand abs"><span class="brand-mark"></span><span class="brand-name">THORNFIELD MARSH, LLC</span></div>
  <div class="contact-chip abs" style="left:627px">
    <div class="chip-icon"><svg width="26" height="26" viewBox="0 0 24 24"><path fill="#fff" d="M6.6 10.8a15.1 15.1 0 0 0 6.6 6.6l2.2-2.2a1 1 0 0 1 1-.25 11.4 11.4 0 0 0 3.6.57 1 1 0 0 1 1 1V20a1 1 0 0 1-1 1A17 17 0 0 1 3 4a1 1 0 0 1 1-1h3.5a1 1 0 0 1 1 1c0 1.25.2 2.45.57 3.57a1 1 0 0 1-.25 1z"/></svg></div>
    <div><div class="chip-label">CALL US</div><div class="chip-value">+1 555 010 0199</div></div>
  </div>
  <div class="contact-chip abs" style="left:908px">
    <div class="chip-icon"><svg width="26" height="26" viewBox="0 0 24 24"><path fill="#fff" d="M3 9l9-6 9 6v10a1 1 0 0 1-1 1H4a1 1 0 0 1-1-1z"/><path fill="#1ea7f0" d="M5 10l7 5 7-5v1l-7 5-7-5z"/></svg></div>
    <div><div class="chip-label">Mail us</div><div class="chip-value">info@thornfieldmarsh.com</div></div>
  </div>
</header>

<nav class="mainnav">
  <a>HOME</a><a>ABOUT US</a><a>ATTORNEY</a><a>PRACTICE AREA</a><a>BLOG</a><a>CONTACT US</a>
</nav>

<section class="hero">
  <div class="hero-photo abs" role="img" aria-label="Three smiling attorneys standing before a glass office tower"></div>
  <h1 class="hero-title abs">A MULTI-SERVICE<br>LAW FIRM</h1>
  <p class="hero-text abs">Lorem ipsum dolor sit amet, consectetur adipiscing elit, sed do eiusmod tempor incididunt ut laboreet dolore magna aliqua.</p>
  <span class="btn btn-sky abs" style="left:58px;top:335px;width:138px;height:32px">CONTACT US</span>
  <span class="btn btn-navy abs" style="left:209px;top:335px;width:138px;height:32px">ABOUT US</span>
</section>

<section class="why">
  <h2 class="section-title abs" style="top:78px">WHY US</h2>
  <div class="title-rule abs" style="left:565px;top:122px;width:70px"></div>

  <div class="feature abs" style="left:190px;top:200px">
    <svg width="56" height="72" viewBox="0 0 56 72" fill="none" stroke="#1ea7f0" stroke-width="2"><path d="M6 4h28l10 10v34H6z"/><path d="M34 4v10h10"/><line x1="12" y1="18" x2="28" y2="18"/><line x1="12" y1="24" x2="32" y2="24"/><circle cx="36" cy="50" r="11" fill="#fff"/><path d="M30 60l-3 10 6-3 3 4 2-10M42 60l3 10-6-3"/></svg>
    <h3>Experienced Attorney</h3>
    <p>Lorem ipsum dolor sit amet, consectetur adipiscing elit, sed do eiusmod tempor incididunt ut laboreet dolore magna aliqua.</p>
    <a>LEARN MORE</a>
  </div>
  <div class="feature abs" style="left:481px;top:200px">
    <svg width="60" height="72" viewBox="0 0 60 72" fill="none" stroke="#1ea7f0" stroke-width="2"><path d="M8 6h32v50H8z"/><path d="M14 4v6M22 4v6M30 4v6"/><line x1="14" y1="20" x2="34" y2="20"/><line x1="14" y1="27" x2="34" y2="27"/><line x1="14" y1="34" x2="34" y2="34"/><line x1="14" y1="41" x2="26" y2="41"/><circle cx="42" cy="54" r="10" fill="#fff"/><path d="M37 54l4 4 6-7"/></svg>
    <h3>Proven Results</h3>
    <p>Lorem ipsum dolor sit amet, consectetur adipiscing elit, sed do eiusmod tempor incididunt ut laboreet dolore magna aliqua.</p>
    <a>LEARN MORE</a>
  </div>
  <div class="feature abs" style="left:771px;top:200px">
    <svg width="70" height="72" viewBox="0 0 70 72" fill="none" stroke="#1ea7f0" stroke-width="2"><path d="M24 12h40v26H44l-8 8v-8H24z"/><path d="M24 28H6v26h8v10l10-10h18v-8"/><circle cx="36" cy="25" r="1.5" fill="#1ea7f0"/><circle cx="44" cy="25" r="1.5" fill="#1ea7f0"/><circle cx="52" cy="25" r="1.5" fill="#1ea7f0"/></svg>
    <h3>Honest Communication</h3>
    <p>Lorem ipsum dolor sit amet, consectetur adipiscing elit, sed do eiusmod tempor incididunt ut laboreet dolore magna aliqua.</p>
    <a>LEARN MORE</a>
  </div>
</section>

<section class="about">
  <svg class="abs" style="left:0;top:0" width="1200" height="478"><polygon points="0,48 0,478 770,478" fill="#0b1f8f"/></svg>
  <div class="about-photo abs" role="img" aria-label="Lawyer and client at a desk with a judge's gavel and an open book"></div>
  <h2 class="about-title abs">THORNFIELD MARSH, LLC</h2>
  <div class="title-rule abs" style="left:622px;top:108px;width:75px;background:var(--gold)"></div>
  <div class="about-text abs">
    <p>Lorem ipsum dolor sit amet, consectetur adipiscing elit, sed do eiusmod tempor incididunt ut labore et dolore magna aliqua. Ut enim ad minim veniam, quis nostrud exercitation ullamco laboris nisi ut aliquip ex ea commodo consequat. Duis aute irure dolor in reprehenderit in voluptate velit esse cillum dolore eu fugiat nulla pariatur.</p>
    <p>Lorem ipsum dolor sit amet, consectetur adipiscing elit, sed do eiusmod tempor incididunt ut labore et dolore magna aliqua. Ut enim ad minim veniam, quis nostrud exercitation ullamco laboris nisi ut aliquip ex ea commodo consequat. Duis aute irure dolor in reprehenderit in voluptate velit esse cillum dolore eu fugiat nulla pariatur.</p>
  </div>
  <span class="btn btn-sky abs" style="left:622px;top:335px;width:137px;height:31px">READ MORE</span>
</section>

<section class="practice">
  <h2 class="section-title abs" style="top:130px">WHAT WE DO</h2>
  <div class="title-rule abs" style="left:565px;top:175px;width:70px"></div>
  <p class="lead abs" style="top:198px">Lorem ipsum dolor sit amet, consectetur adipiscing elit, sed do eiusmod tempor incididunt ut labore<br>et dolore magna aliqua. Ut enim ad minim veniam.</p>

  <div class="practice-card abs" style="left:101px;width:482px">
    <div class="practice-photo" role="img" aria-label="Hands reviewing legal documents beside a gavel" style="background:linear-gradient(135deg,#3a3a3a,#b9c3cf 60%,#e8ecf1)"></div>
    <div class="practice-body">
      <h3>MULTIDISTRICT LITIGATION</h3>
      <p>Lorem ipsum dolor sit amet, consectetur adipiscing elit, sed do eiusmod tempor incididunt ut labore et dolore magna aliqua. Ut enim ad minim veniam, quis nostrud exercitation ullamco laboris nisi ut aliquip ex ea commodo consequat. Duis aute irure dolor in reprehenderit in voluptate velit esse cillum dolore eu fugiat nulla pariatur.</p>
      <span class="btn btn-sky">READ MORE</span>
    </div>
  </div>
  <div class="practice-card abs" style="left:610px;width:485px">
    <div class="practice-photo" role="img" aria-label="Hand signing a contract with a pen" style="background:linear-gradient(135deg,#5a5a5a,#a8a8a8 50%,#e3e3e3)"></div>
    <div class="practice-body" style="padding-top:38px">
      <h3>CLASS ACTIONS</h3>
      <p>Lorem ipsum dolor sit amet, consectetur adipiscing elit, sed do eiusmod tempor incididunt ut labore et dolore magna aliqua. Ut enim ad minim veniam, quis nostrud exercitation ullamco laboris nisi ut aliquip ex ea commodo consequat. Duis aute irure dolor in reprehenderit in voluptate velit esse cillum dolore eu fugiat nulla pariatur.</p>
      <span class="btn btn-sky">READ MORE</span>
    </div>
  </div>
</section>

<section class="team">
  <div class="abs" style="left:466px;top:87px;width:232px;height:3px;background:var(--gold)"></div>
  <h2 class="section-title abs" style="top:118px;color:var(--white)">OUR TEAM</h2>

  <div class="member abs" style="left:173px">
    <div class="avatar" role="img" aria-label="Portrait photo of Leonard Thornfield"></div>
    <h3>LEONARD THORNFIELD</h3>
    <span class="role">Attorney</span>
    <p>Lorem ipsum dolor sit amet, consectetur adipiscing elit, sed do eiusmod tempor incididunt ut labore et dolore magna aliqua.</p>
  </div>
  <div class="member abs" style="left:464px">
    <div class="avatar" role="img" aria-label="Portrait photo of Brent Marsh"></div>
    <h3>BRENT MARSH</h3>
    <span class="role">Attorney</span>
    <p>Lorem ipsum dolor sit amet, consectetur adipiscing elit, sed do eiusmod tempor incididunt ut labore et dolore magna aliqua.</p>
  </div>
  <div class="member abs" style="left:755px">
    <div class="avatar" role="img" aria-label="Portrait photo of Melinda Carrow"></div>
    <h3>MELINDA CARROW</h3>
    <span class="role">Legal Assistant</span>
    <p>Lorem ipsum dolor sit amet, consectetur adipiscing elit, sed do eiusmod tempor incididunt ut labore et dolore magna aliqua.</p>
  </div>
</section>

<section class="blog">
  <h2 class="section-title abs" style="top:105px">BLOG NEWS</h2>
  <div class="title-rule abs" style="left:538px;top:155px;width:115px"></div>
  <p class="lead abs" style="top:200px">Lorem ipsum dolor sit amet, consectetur adipiscing elit, sed do eiusmod tempor incididunt ut labore<br>et dolore magna aliqua. Ut enim ad minim veniam.</p>

  <article class="post abs" style="left:173px">
    <div class="post-photo" role="img" aria-label="Bronze justice statue and gavel on a white table" style="background:linear-gradient(120deg,#e9e9e9,#cfcfcf 60%,#7b4a2e)"></div>
    <h3>Blog Post Title</h3>
    <div class="post-meta"><span>▣ April 4, 2025</span><span>● Admin</span></div>
    <p>Lorem ipsum dolor sit amet, consectetur adipiscing elit, sed do eiusmod tempor incididunt ut labore et dolore magna aliqua.</p>
  </article>
  <article class="post abs" style="left:477px">
    <div class="post-photo" role="img" aria-label="Three colleagues in suits reviewing papers in an office" style="background:linear-gradient(120deg,#c8cdd3,#5d6470 55%,#2b2f36)"></div>
    <h3>Blog Post Title</h3>
    <div class="post-meta"><span>▣ April 4, 2025</span><span>● Admin</span></div>
    <p>Lorem ipsum dolor sit amet, consectetur adipiscing elit, sed do eiusmod tempor incididunt ut labore et dolore magna aliqua.</p>
  </article>
  <article class="post abs" style="left:781px">
    <div class="post-photo" role="img" aria-label="Stone columns of a courthouse in warm light" style="background:linear-gradient(120deg,#8a8fa0,#d6b46a 50%,#a9823f)"></div>
    <h3>Blog Post Title</h3>
    <div class="post-meta"><span>▣ April 4, 2025</span><span>● Admin</span></div>
    <p>Lorem ipsum dolor sit amet, consectetur adipiscing elit, sed do eiusmod tempor incididunt ut labore et dolore magna aliqua.</p>
  </article>
</section>

<footer class="site-footer">
  <div class="foot-brand abs"><span class="brand-mark"></span><span class="brand-name">THORNFIELD MARSH, LLC</span></div>
  <p class="foot-about abs">Lorem ipsum dolor sit amet, consectetur adipiscing elit, sed do eiusmod temporincididunt ut labore et dolore magna aliqua.</p>
  <div class="social abs" aria-label="Social links"><span></span><span></span><span></span></div>

  <div class="abs" style="left:471px;top:110px">
    <div class="foot-head">QUICK LINKS</div>
    <ul class="foot-links">
      <li><svg width="14" height="14" viewBox="0 0 14 14" fill="none" stroke="#1ea7f0" stroke-width="1.5"><circle cx="7" cy="7" r="6"/><path d="M5 4l3 3-3 3"/></svg>Home</li>
      <li><svg width="14" height="14" viewBox="0 0 14 14" fill="none" stroke="#1ea7f0" stroke-width="1.5"><circle cx="7" cy="7" r="6"/><path d="M5 4l3 3-3 3"/></svg>About</li>
      <li><svg width="14" height="14" viewBox="0 0 14 14" fill="none" stroke="#1ea7f0" stroke-width="1.5"><circle cx="7" cy="7" r="6"/><path d="M5 4l3 3-3 3"/></svg>Attorney</li>
      <li><svg width="14" height="14" viewBox="0 0 14 14" fill="none" stroke="#1ea7f0" stroke-width="1.5"><circle cx="7" cy="7" r="6"/><path d="M5 4l3 3-3 3"/></svg>Blog</li>
      <li><svg width="14" height="14" viewBox="0 0 14 14" fill="none" stroke="#1ea7f0" stroke-width="1.5"><circle cx="7" cy="7" r="6"/><path d="M5 4l3 3-3 3"/></svg>Contact</li>
    </ul>
  </div>

  <div class="abs" style="left:678px;top:110px">
    <div class="foot-head">CONTACT</div>
    <ul class="foot-contact">
      <li><svg width="16" height="16" viewBox="0 0 24 24"><path fill="#1ea7f0" d="M6.6 10.8a15.1 15.1 0 0 0 6.6 6.6l2.2-2.2a1 1 0 0 1 1-.25 11.4 11.4 0 0 0 3.6.57 1 1 0 0 1 1 1V20a1 1 0 0 1-1 1A17 17 0 0 1 3 4a1 1 0 0 1 1-1h3.5a1 1 0 0 1 1 1c0 1.25.2 2.45.57 3.57a1 1 0 0 1-.25 1z"/></svg>(+1) 555 014 2270</li>
      <li><svg width="16" height="16" viewBox="0 0 24 24"><path fill="#1ea7f0" d="M2 6h20v13H2z"/><path fill="none" stroke="#121212" stroke-width="2" d="M2 7l10 7 10-7"/></svg>help@thornfieldmarsh.com</li>
      <li><svg width="16" height="16" viewBox="0 0 24 24"><path fill="#1ea7f0" d="M12 2a7 7 0 0 0-7 7c0 5 7 13 7 13s7-8 7-13a7 7 0 0 0-7-7z"/><circle cx="12" cy="9" r="2.5" fill="#121212"/></svg>48 Alder Row, Brookhaven</li>
    </ul>
  </div>

  <div class="abs" style="left:935px;top:110px">
    <div class="foot-head">SUBSCRIBE</div>
    <div class="subscribe-field"></div>
    <div class="subscribe-btn">SUBSCRIBE NOW</div>
  </div>

  <div class="foot-rule abs"></div>
  <p class="copyright abs">Copyright © 2025, Thornfield Marsh LLC. All Rights Reserved.</p>
</footer>

</body>
</html>
```